Church Website with Home Page and Member Sermon Library

I am in need of an updated design for our church website. This will include 4 pages (outlined below). We are a conservative, evangelical, Christian church. The site should be modern and clean, while still reflecting our conservative values. I already have a logo for our church, and I want the site to incorporate the logo, and match the logo/branding. Stock photos are allowed if needed, but I have uploaded some images of our church and would prefer those images to be used if possible. Any stock photos used should not include any people in the photos (scenery, nature, buildings, animals, etc. are fine).

The site will need 4 pages: Home, Support Us (Donate), Login, and Recording Library.

Page 1: Home
The home page should include the following sections:

- Navigation: Should include links to each section of the home page plus a "listen live" link which will take the user to a live-streaming site and a "support us" link which will take the user to a support/donate page.

- Announcements: Can be either a banner or some other design, but there needs to be some way for us to post announcements for visitors to see. I'm open for creative ideas in this section, but would like it not to take up a lot of room on the page.

- About Us: Should include address, service times (see attached document), and information about the church.

- Pastor Bio: A section that introduces our pastor and gives a short bio about our pastor. Would like this section to include a picture of our pastor. Somewhere in this section I would like to include this Bible reference: "And I will give you pastors according to mine heart, which shall feed you with knowledge and understanding. Jer 3:15 KJV"

- Articles of Faith (What We Believe): This should include several sub-sections each with a heading, body, and possibly 1 or more scripture references. I have attached a document to the brief that includes our articles of faith. Feel free to be creative with this section in how you lay these out and format them.

- Support Us: A small section that explains what kind of support someone can give and a link to a donation page. The link can say something like "Support Us" or "Donate Now".

- Contact form: A contact form that allows the visitor to send us a message. The contact form should ask for name, email, phone, and message.

- Footer: A footer that will be displayed on all pages of the site. This should include at a minimum a link to the home page (or a link to each individual section in the home page if you prefer), a link to "listen live", a link to "support us", a link to "contact us" (or you can put the contact form directly in the footer if you prefer), the address, and a "member login" link.

Page 2: Support Us
The donation page should include a form the visitor can fill out to make a donation. We will embed a third party form later. For this design, please just mock out the design with a basic form asking for name, phone, and email.

Page 3: Login
The recording library (detailed below) will require members to login with a shared numeric code before accessing the page. We need a design for a login screen. The screen should include navigation/footer just like all other pages, but the body of the login page will consist only of a form that asks the user to enter the access code and then a "login" button.

Page 4: Recording Library

The library page is a member-only page that will require a shared, numeric pass code to access. On this page, members will be able to access a filterable list of past sermons. The page by default should display most recent sermons, but should also include a search form that allows the member to filter the sermon list to find a particular sermon. The search form should allow the user to select a filter type (e.g. Speaker name, date, event, etc.) and type in a value to search. They should be able to add multiple filters and remove filters that have been added. Each sermon that is displayed in the result list should include basic information such as title, date, speaker, tags, etc. along with a download icon, and an embedded audio player where they can click a play button to stream it on-demand. Each sermon should also have clickable tags associated with it that can be used to find related sermons.
Updates

I have uploaded several images of our church. Feel free to incorporate these into your design if possible.

Target Market(s)

Church Members

Industry/Entity Type

Religion

Number of Pages Required

4 page

Font styles to use
Sans Serif

Colors

Designer to choose colors to be used in the design.

Requirements
Must have
• Must incorporate the logo (attached)
Nice to have
• Would like the design to incorporate pictures of our church (attached) instead of stock photos if possible.
Should not have
• Please avoid an overly cluttered design. Stock photos used should not include any people in the photos.

```html
<!DOCTYPE html>
<html lang="en">
<head>
<meta charset="utf-8">
<title>Recording Library – Grace Harbor Church</title>
<link href="https://fonts.googleapis.com/css2?family=Cormorant+Garamond:wght@600;700&family=Open+Sans:wght@400;600&display=swap" rel="stylesheet">
<style>
:root{
  --green:#86a86a;
  --cyan:#17aacd;
  --ink:#2c2c2c;
  --card:#ecf0ea;
  --line:#d6ddd2;
  --footer:#353535;
  --white:#fff;
  --muted:#b9b9b9;
}
*{margin:0;padding:0;box-sizing:border-box}
html,body{width:933px;height:1200px;overflow:hidden;background:var(--white)}
body{position:relative;font-family:"Open Sans",sans-serif;color:var(--ink)}
.abs{position:absolute}
.header{left:0;top:0;width:933px;height:64px;background:var(--white)}
.brand{left:112px;top:15px;width:80px;text-align:center;color:var(--green);font-size:11px;line-height:13px;letter-spacing:1px}
.brand .dot{display:block;width:12px;height:12px;border-radius:50%;background:var(--cyan);margin:0 auto 4px}
.nav{top:27px;font-size:8.6px;letter-spacing:.4px}
.nav a{position:absolute;color:var(--ink);text-decoration:none;white-space:nowrap}
.pill{display:flex;align-items:center;gap:4px;color:var(--white);font-size:8.5px;line-height:8.5px;border-radius:2px;padding:0 4px;text-decoration:none}
.pill.listen{background:var(--green)}
.pill.support{background:var(--cyan)}
.hero{left:0;top:64px;width:933px;height:193px;background:linear-gradient(100deg,#6e5447 0%,#8a6a58 35%,#7b6a60 60%,#9a9490 100%)}
.hero-rule{left:121px;top:166px;width:60px;height:1px;background:var(--white)}
.hero-title{left:194px;top:148px;font-family:"Cormorant Garamond",serif;font-weight:700;font-size:29px;line-height:36px;color:var(--white);letter-spacing:.3px}
.crumbs{left:121px;top:226px;font-size:12px;color:var(--white)}
.crumbs span{margin:0 10px}
.cat{left:155px;top:285px;font-family:"Cormorant Garamond",serif;font-weight:700;font-size:21px;line-height:28px;color:#3a3a3a}

.filter-form{left:437px;top:285px;height:26px;display:flex;gap:6px}
.filter-form .field{height:26px;border:1px solid var(--line);background:var(--card);font-size:8.8px;color:#6d6d6d;display:flex;align-items:center;padding:0 8px;border-radius:2px}
.filter-form .type{width:96px;justify-content:space-between}
.filter-form .value{width:150px}
.filter-form .add{width:80px;justify-content:center;background:var(--green);border-color:var(--green);color:var(--white);font-weight:600;letter-spacing:.3px}
.chips{left:153px;top:320px;display:flex;align-items:center;gap:6px;font-size:8.5px}
.chips .label{color:#6d6d6d;margin-right:2px}
.chip{display:flex;align-items:center;gap:6px;height:18px;padding:0 8px;border-radius:9px;background:var(--card);color:var(--ink)}
.chip b{font-weight:600;color:var(--green)}
.chip .x{color:#8a8a8a;font-size:10px;line-height:10px}
.chips .clear{color:var(--cyan);margin-left:4px}

.track{left:153px;width:624px;height:110px;background:var(--card)}
.disc{left:38px;top:11px;width:88px;height:88px;border-radius:50%;background:radial-gradient(circle,#6b5040 0%,#3a2a22 55%,#1e1612 100%)}
.play{position:absolute;left:24px;top:24px;width:40px;height:40px;border-radius:50%;background:rgba(255,255,255,.85)}
.play svg{position:absolute;left:14px;top:11px}
.speaker{left:143px;top:19px;font-size:8.8px;color:var(--green);display:flex;align-items:center;gap:4px}
.title{left:142px;top:33px;font-family:"Cormorant Garamond",serif;font-weight:700;font-size:19px;line-height:24px;color:#2e2e2e;white-space:nowrap}
.bar{left:142px;top:68px;width:306px;height:13px;border-radius:7px;background:var(--white)}
.time{left:463px;top:68px;font-size:9.5px;color:var(--ink)}
.vol-icon{left:505px;top:67px}
.vol{left:537px;top:68px;width:49px;height:13px;border-radius:7px;background:var(--white)}
.vol i{position:absolute;left:5px;top:4px;width:28px;height:5px;border-radius:3px;background:var(--green)}
.pager{left:445px;top:833px;display:flex;align-items:center;gap:6px;font-size:9.5px;color:var(--muted)}
.pager .on{width:18px;height:18px;background:var(--green);color:var(--white);display:flex;align-items:center;justify-content:center;font-weight:600;border-radius:1px}
.footer{left:0;top:871px;width:933px;height:329px;background:var(--footer)}
.f-brand{left:0;width:933px;top:100px;text-align:center;color:var(--green);font-size:17px;letter-spacing:1.5px}
.f-brand .dot{display:block;width:16px;height:16px;border-radius:50%;background:var(--cyan);margin:0 auto 8px}
.f-nav{left:0;width:933px;top:201px;display:flex;justify-content:center;font-size:8.8px;font-weight:600;color:var(--white);letter-spacing:.3px}
.f-nav span{padding:0 10px;border-left:1px solid var(--green);line-height:11px}
.f-nav span:first-child{border-left:none}
.f-btns{left:0;width:933px;top:237px;display:flex;justify-content:center;gap:9px}
.copy{left:0;width:933px;top:1172px;text-align:center;font-size:8.8px;color:#bdbdbd}
</style>
</head>
<body>

<header class="abs header">
  <div class="abs brand"><span class="dot"></span>GRACE<br>HARBOR</div>
  <nav class="abs nav">
    <a style="left:283px">HOME</a>
    <a style="left:332px">ANNOUNCEMENTS</a>
    <a style="left:434px">ABOUT US</a>
    <a style="left:504px">PASTOR BIO</a>
    <a style="left:581px">ARTICLES OF FAITH</a>
  </nav>
  <a class="abs pill listen" style="left:679px;top:20px;width:55px;height:26px">
    <svg width="14" height="14" viewBox="0 0 14 14" fill="none" stroke="#fff" stroke-width="1.3"><path d="M2 9V7a5 5 0 0 1 10 0v2"/><rect x="1" y="9" width="12" height="4" rx="1"/></svg>
    <span>listen<br>live</span></a>
  <a class="abs pill support" style="left:743px;top:20px;width:63px;height:26px">
    <svg width="16" height="14" viewBox="0 0 16 14" fill="none" stroke="#fff" stroke-width="1.2"><path d="M8 13 2 7a3 3 0 0 1 6-4 3 3 0 0 1 6 4z"/></svg>
    <span>Support<br>Us</span></a>
</header>

<section class="abs hero" role="img" aria-label="Brick church wall with the church's service-times sign"></section>
<div class="abs hero-rule"></div>
<h1 class="abs hero-title">Recording Library</h1>
<div class="abs crumbs">Home<span>›</span>Recording-Library</div>

<h2 class="abs cat">Catagory Name</h2>

<form class="abs filter-form" aria-label="Filter sermons">
  <div class="field type">Speaker
    <svg width="8" height="5" viewBox="0 0 8 5"><path d="M0 0 4 5 8 0z" fill="#86a86a"/></svg></div>
  <div class="field value">Type a value to search…</div>
  <div class="field add">+ ADD FILTER</div>
</form>

<div class="abs chips">
  <span class="label">Active filters:</span>
  <span class="chip"><b>Speaker:</b> Daniel Reeves <span class="x">×</span></span>
  <span class="chip"><b>Tag:</b> Hebrews <span class="x">×</span></span>
  <span class="clear">Clear all</span>
</div>

<article class="abs track" style="top:346px">
  <div class="abs disc" role="img" aria-label="Church sanctuary interior"><div class="play"><svg width="16" height="18" viewBox="0 0 16 18"><path d="M0 0 16 9 0 18z" fill="#86a86a"/></svg></div></div>
  <div class="abs speaker"><svg width="8" height="9" viewBox="0 0 8 9" fill="#86a86a"><circle cx="4" cy="2.3" r="2.2"/><path d="M0 9a4 4 0 0 1 8 0z"/></svg>Daniel Reeves</div>
  <h3 class="abs title">Jesus, A Power Greater than the Angels</h3>
  <div class="abs bar"></div><div class="abs time">-28:33</div>
  <svg class="abs vol-icon" width="17" height="14" viewBox="0 0 17 14"><path d="M0 4h3l5-4v14L3 10H0z" fill="#111"/><path d="M11 4a4 4 0 0 1 0 6M13.5 2a7 7 0 0 1 0 10" stroke="#111" stroke-width="1.5" fill="none"/></svg>
  <div class="abs vol"><i></i></div>
</article>

<article class="abs track" style="top:463px">
  <div class="abs disc" role="img" aria-label="Church sanctuary interior"><div class="play"><svg width="16" height="18" viewBox="0 0 16 18"><path d="M0 0 16 9 0 18z" fill="#86a86a"/></svg></div></div>
  <div class="abs speaker"><svg width="8" height="9" viewBox="0 0 8 9" fill="#86a86a"><circle cx="4" cy="2.3" r="2.2"/><path d="M0 9a4 4 0 0 1 8 0z"/></svg>Daniel Reeves</div>
  <h3 class="abs title">Jesus, A Power Greater than the Angels</h3>
  <div class="abs bar"></div><div class="abs time">-28:33</div>
  <svg class="abs vol-icon" width="17" height="14" viewBox="0 0 17 14"><path d="M0 4h3l5-4v14L3 10H0z" fill="#111"/><path d="M11 4a4 4 0 0 1 0 6M13.5 2a7 7 0 0 1 0 10" stroke="#111" stroke-width="1.5" fill="none"/></svg>
  <div class="abs vol"><i></i></div>
</article>

<article class="abs track" style="top:580px">
  <div class="abs disc" role="img" aria-label="Church sanctuary interior"><div class="play"><svg width="16" height="18" viewBox="0 0 16 18"><path d="M0 0 16 9 0 18z" fill="#86a86a"/></svg></div></div>
  <div class="abs speaker"><svg width="8" height="9" viewBox="0 0 8 9" fill="#86a86a"><circle cx="4" cy="2.3" r="2.2"/><path d="M0 9a4 4 0 0 1 8 0z"/></svg>Daniel Reeves</div>
  <h3 class="abs title">Jesus, A Power Greater than the Angels</h3>
  <div class="abs bar"></div><div class="abs time">-28:33</div>
  <svg class="abs vol-icon" width="17" height="14" viewBox="0 0 17 14"><path d="M0 4h3l5-4v14L3 10H0z" fill="#111"/><path d="M11 4a4 4 0 0 1 0 6M13.5 2a7 7 0 0 1 0 10" stroke="#111" stroke-width="1.5" fill="none"/></svg>
  <div class="abs vol"><i></i></div>
</article>

<article class="abs track" style="top:697px">
  <div class="abs disc" role="img" aria-label="Church sanctuary interior"><div class="play"><svg width="16" height="18" viewBox="0 0 16 18"><path d="M0 0 16 9 0 18z" fill="#86a86a"/></svg></div></div>
  <div class="abs speaker"><svg width="8" height="9" viewBox="0 0 8 9" fill="#86a86a"><circle cx="4" cy="2.3" r="2.2"/><path d="M0 9a4 4 0 0 1 8 0z"/></svg>Daniel Reeves</div>
  <h3 class="abs title">Jesus, A Power Greater than the Angels</h3>
  <div class="abs bar"></div><div class="abs time">-28:33</div>
  <svg class="abs vol-icon" width="17" height="14" viewBox="0 0 17 14"><path d="M0 4h3l5-4v14L3 10H0z" fill="#111"/><path d="M11 4a4 4 0 0 1 0 6M13.5 2a7 7 0 0 1 0 10" stroke="#111" stroke-width="1.5" fill="none"/></svg>
  <div class="abs vol"><i></i></div>
</article>

<div class="abs pager"><span class="on">1</span><span>2</span><span>3</span></div>

<footer class="abs footer">
  <div class="abs f-brand"><span class="dot"></span>GRACE HARBOR<br><span style="font-size:7px;letter-spacing:5px">CHURCH</span></div>
  <nav class="abs f-nav"><span>HOME</span><span>ANNOUNCEMENTS</span><span>ABOUT US</span><span>PASTOR BIO</span><span>ARTICLES OF FAITH</span><span>CONTACT US</span></nav>
  <div class="abs f-btns">
    <a class="pill listen" style="width:55px;height:26px">
      <svg width="14" height="14" viewBox="0 0 14 14" fill="none" stroke="#fff" stroke-width="1.3"><path d="M2 9V7a5 5 0 0 1 10 0v2"/><rect x="1" y="9" width="12" height="4" rx="1"/></svg>
      <span>listen<br>live</span></a>
    <a class="pill support" style="width:63px;height:26px">
      <svg width="16" height="14" viewBox="0 0 16 14" fill="none" stroke="#fff" stroke-width="1.2"><path d="M8 13 2 7a3 3 0 0 1 6-4 3 3 0 0 1 6 4z"/></svg>
      <span>Support<br>Us</span></a>
  </div>
</footer>
<div class="abs copy">© 2023 Grace Harbor Church. All rights reserved. Privacy Policy</div>

</body>
</html>
```